Corporate Design - Immobilienverwaltungsgesellschaft
Zielgruppe
An- und Verkauf, Verwaltung und Vermietung von Immobilien
Zielgruppen: Immobilienspekulanten, Wohnungskäufer, Mieter, Vermieter
Aufgabenstellung
Wir suchen ein hochwertiges Design für eine in Gründung befindliche Gesellschaft mit beschränkter Haftung.
Diese wird aus 2 Gesellschaftern, Katrin und Thomas Brelm bestehen.
Das Hauptziel der Gesellschaft wird der An- und Verkauf von Immobilien bis zu 1. Million Euro je Kaufobjekt sein
Mit dem Nachnamen der Gesellschafter kann auch gespielt werden, beispielsweise bei Abkürzungen. Die Bezeichnung B&B Verwaltungsgesellschaft mbH ist nicht zwingend, lediglich das Kürzel 'mbH' oder auch 'GmbH' ist aufgrund der Rechtsform der Gesellschaft zwingend aufzunehmen.
Diverse Designideen haben wir bereits vorliegen; hierauf kann aufgebaut werden, siehe Uploads
Unter anderem eine Anlehnung an die unter derselben Firmenadresse der Gesellschaft bestehende Rechtsanwaltskanzlei und deren Cooperate Design wäre eine Idee, jedoch keine zwingende Voraussetzung.

```html
<!DOCTYPE html>
<html lang="de">
<head>
<meta charset="utf-8">
<title>B&amp;B Verwaltungsgesellschaft mbH – Briefbogen</title>
<link href="https://fonts.googleapis.com/css2?family=Fira+Sans+Condensed:wght@400;600&family=Fira+Sans:wght@400;600&display=swap" rel="stylesheet">
<style>
  :root {
    --backdrop: #34404f;
    --paper: #ffffff;
    --ink: #1f1f1f;
    --brand-blue: #0a7cc1;
    --brand-navy: #0d4b8c;
    --band-dark: #3c3c3e;
    --fold-mark: #b8bcc2;
  }
  * { margin: 0; padding: 0; box-sizing: border-box; }
  html, body {
    width: 894px; height: 1200px; overflow: hidden;
    background: var(--backdrop);
  }
  .letterhead {
    position: absolute; left: 37px; top: 20px;
    width: 820px; height: 1160px;
    background: var(--paper);
    overflow: hidden;
    font-family: "Fira Sans Condensed", "Arial Narrow", sans-serif;
    color: var(--ink);
  }
  .brand {
    position: absolute; right: 40px; top: 70px;
    display: flex; align-items: center; gap: 10px;
  }
  .brand-square { width: 14px; height: 14px; background: var(--brand-navy); }
  .brand-name {
    font-weight: 600; font-size: 21px; color: var(--brand-navy);
    letter-spacing: 0.2px;
  }
  .sender-line {
    position: absolute; left: 97px; top: 176px;
    font-size: 9.5px; padding-bottom: 2px;
    border-bottom: 1.5px solid var(--brand-blue);
  }
  .info-column {
    position: absolute; left: 619px; top: 177px; height: 186px;
    border-left: 1.5px solid var(--brand-navy);
    padding-left: 15px;
    font-family: "Fira Sans", sans-serif; font-size: 10.2px; line-height: 15.3px;
  }
  .info-column p { margin-bottom: 11.6px; }
  .info-column p:last-child { margin-bottom: 0; }
  .manager { color: var(--brand-blue); font-weight: 600; }
  .contact-row { display: flex; align-items: center; gap: 6px; }
  .contact-row svg { width: 11px; height: 11px; fill: var(--brand-blue); flex: none; }
  .fold-mark { position: absolute; left: 0; height: 1px; background: var(--fold-mark); }
  .footer-rule {
    position: absolute; left: 0; top: 1076px; width: 820px; height: 6px;
    background: var(--brand-blue);
  }
  .footer-band {
    position: absolute; left: 0; top: 1086px; width: 820px; height: 74px;
    background: var(--band-dark);
  }
  .bank-details {
    position: absolute; left: 82px; top: 1116px;
    font-size: 10px; color: #fff;
  }
  .bank-details strong { font-weight: 600; }
  .bank-details .sep { color: var(--brand-blue); }
</style>
</head>
<body>
<main class="letterhead">
  <div class="brand">
    <span class="brand-square"></span>
    <span class="brand-name">B&amp;B Verwaltungsgesellschaft mbH</span>
  </div>

  <div class="sender-line">B&amp;B Verwaltungsgesellschaft mbH • Am Lindenhof 17 •&nbsp; 66111 Musterstadt</div>

  <aside class="info-column">
    <p>Geschäftsführer:<br>
      <span class="manager">Katrin Brelm</span><br>
      <span class="manager">Thomas Brelm</span></p>
    <p>Am Lindenhof 17<br>66111 Musterstadt</p>
    <p>
      <span class="contact-row"><svg viewBox="0 0 24 24"><path d="M6.6 10.8a15 15 0 0 0 6.6 6.6l2.2-2.2a1 1 0 0 1 1-.25 11.4 11.4 0 0 0 3.6.6 1 1 0 0 1 1 1V20a1 1 0 0 1-1 1A17 17 0 0 1 3 4a1 1 0 0 1 1-1h3.5a1 1 0 0 1 1 1c0 1.25.2 2.45.6 3.6a1 1 0 0 1-.25 1z"/></svg>01234 / 765 432</span>
      <span class="contact-row"><svg viewBox="0 0 24 24"><path d="M6 2h12v6H6zM8 4v4h8V4zM3 9h18a1 1 0 0 1 1 1v8h-4v4H6v-4H2v-8a1 1 0 0 1 1-1zm5 7v4h8v-4z"/></svg>01234 / 765 432</span>
      <span class="contact-row"><svg viewBox="0 0 24 24"><path d="M2 5h20v14H2zm2 2v.5l8 5 8-5V7l-8 5z"/></svg>info@bundb-verwaltung.de</span>
      <span class="contact-row"><svg viewBox="0 0 24 24"><path d="M12 2a10 10 0 1 0 0 20 10 10 0 0 0 0-20zm-1 2.1V8H7.6A8 8 0 0 1 11 4.1zm2 0A8 8 0 0 1 16.4 8H13zM6.6 10H11v4H6.6a8 8 0 0 1 0-4zm6.4 0h4.4a8 8 0 0 1 0 4H13zm-5.4 6H11v3.9A8 8 0 0 1 7.6 16zm5.4 0h3.4a8 8 0 0 1-3.4 3.9z"/></svg>www.bundb-verwaltung.de</span>
    </p>
    <p>USt-IdNr. DE123456789</p>
  </aside>

  <span class="fold-mark" style="top:410px;width:25px"></span>
  <span class="fold-mark" style="top:580px;width:39px"></span>
  <span class="fold-mark" style="top:808px;width:25px"></span>

  <div class="footer-rule"></div>
  <div class="footer-band"></div>

  <div class="bank-details"><strong>Bankverbindung:</strong> Kreisbank Musterstadt <span class="sep">•</span> BIC: KRBMDE12XXX <span class="sep">•</span> IBAN: DE98 7654 3210 9876 54321</div>
</main>
</body>
</html>
```